Greyfield Ridge Medical Website to make connecting and communicating easier

To create a unique, user-friendly, professional website for patients and professionals to access education/ information, forms, appointments, contact details, and data about us, and for us to have the capacity to link to various cloud-based platforms.
To use the logo design and colour scheme we have just sourced.

WEBSITE to be eye catching, Inspiring and alluring
- efficient and logical
- professional and trustworthy appearance
- health focus "living health matters"
- user friendly
- ability to link with cloud-based software and video conferencing tools/ telehealth
- colours- black/ white teal and ?silver

PAGES:
page 1 - Our clinic and staff, services offered, contact us- address/ map / contact details- social media connections
page 2- patients and visitors - New patient forms to complete, news and patient informtion (educatinal)
page 3 - health professionals -referral forms, research and education
page 3- online appointments
page 4 - Quick links - partners, other services
page 5- privacy policy, disclaimer

HI, Could we please extend the deadline another 5 days, so sorry just struggling with my workload to be able to keep up and I am wanting to liaise more with the designer that I will choose. I am so happy with PixelHarbor and all the designers - thank you! Thank you so much!!

Target Market(s)

Patients - mostly over 60's so the website must be minimal clicks and simple to navigate
Professionals - for education and access forms

Industry/Entity Type

Health Care

Coding

Coded - Design and coding required

Number of Pages Required

5+ page

Font styles to use
Sans Serif
Script

Colors
33b8a4
86cfc6

Requirements
Must have
• WEBSITE to be eye catching, Inspiring and alluring
- efficient and logical
- user friendly

WEBSITE - professional and user friendly
- ability to link with cloud based software and videoconferencing/ telehealth
Nice to have
• clean and crisp presentation
happy for an innovative look
room to add more services and ability to link pages and resources
Should not have
• Please ensure the website is not:
clunky
difficult to navigate
common and cheap looking

```html
<!DOCTYPE html>
<html lang="en">
<head>
<meta charset="utf-8">
<title>About Our Practice – Greyfield Ridge Medical</title>
<link href="https://fonts.googleapis.com/css2?family=Montserrat:wght@600;700&family=Mulish:wght@400;600&display=swap" rel="stylesheet">
<style>
:root{
  --teal:#1f9b8a;
  --teal-bright:#33b8a4;
  --teal-soft:#86cfc6;
  --ink:#1d3a38;
  --text:#222;
  --muted:#5a5a5a;
  --bar:#f6f6f6;
  --band:#fafafa;
  --foot:#f3f3f3;
  --white:#fff;
}
*{box-sizing:border-box;margin:0;padding:0}
html,body{width:1200px;height:1200px;overflow:hidden;background:#fff}
body{font-family:'Mulish',sans-serif;color:var(--text);position:relative}
.page{position:absolute;left:284px;top:0;width:960px;height:1825px;transform:scale(.6575);transform-origin:0 0;background:#fff}
.abs{position:absolute}
/* header */
.topbar{left:0;top:0;width:960px;height:86px;background:var(--bar)}
.brand{display:flex;align-items:center;gap:8px;font-family:'Mulish',sans-serif;font-weight:600;color:var(--teal-bright);font-size:18px;line-height:1.1;white-space:nowrap}
.brand .dot{width:14px;height:14px;border-radius:50%;background:var(--teal-bright);flex:none}
.topbar .brand{position:absolute;left:64px;top:32px}
.contact-line{display:flex;align-items:center;gap:7px;font-size:11px;color:var(--text);white-space:nowrap}
.topbar .mail{position:absolute;left:596px;top:36px}
.topbar .phone{position:absolute;left:790px;top:36px}
.nav{left:64px;top:108px;width:832px;display:flex;justify-content:space-between;font-size:12.5px;letter-spacing:.2px}
.nav a{color:var(--text);text-decoration:none}
.nav a.current{color:var(--teal-bright)}
.hero{left:0;top:146px;width:960px;height:225px;background:linear-gradient(90deg,#dfe6ea 0%,#c4d2da 35%,#a9bccb 52%,#5f8fbf 72%,#4f86b9 85%,#7aa6d6 100%)}
.hero h1{position:absolute;left:134px;top:62px;font-family:'Montserrat',sans-serif;font-weight:700;font-size:35px;line-height:36px;color:var(--ink)}
.hero h1 span{display:block;color:var(--teal)}
/* intro */
.section-title{font-family:'Montserrat',sans-serif;font-weight:600;font-size:30px;color:var(--ink);text-align:center;width:960px;left:0}
.rule{height:3px;width:53px;background:var(--teal)}
.lede{font-size:12px;color:var(--teal)}
.body-copy{font-size:12.3px;line-height:18px;color:var(--muted)}
/* team */
.team-band{left:0;top:660px;width:960px;height:858px;background:var(--band)}
.card{width:192px;height:243px;background:var(--white);box-shadow:0 1px 5px rgba(0,0,0,.14);border-radius:3px;overflow:hidden}
.card .photo{height:175px}
.photo.coat{background:radial-gradient(ellipse 38% 55% at 50% 38%,#e6dcd3 0%,rgba(230,220,211,0) 100%),linear-gradient(180deg,#ffffff 0%,#f4f6f7 58%,#e9eef0 72%,#cfdde2 86%,#5aa99f 100%)}
.photo.coat-blue{background:radial-gradient(ellipse 38% 55% at 50% 38%,#e3d7cc 0%,rgba(227,215,204,0) 100%),linear-gradient(180deg,#ffffff 0%,#f4f6f7 58%,#e6edf2 74%,#b9cde0 88%,#7d9cc2 100%)}
.photo.scrubs{background:radial-gradient(ellipse 38% 55% at 50% 38%,#e2d2c4 0%,rgba(226,210,196,0) 100%),linear-gradient(180deg,#ffffff 0%,#f5f7f7 60%,#bfe3dc 80%,#6cc2b4 100%)}
.photo.scrubs-soft{background:radial-gradient(ellipse 38% 55% at 50% 38%,#dcc8b6 0%,rgba(220,200,182,0) 100%),linear-gradient(180deg,#ffffff 0%,#f5f7f7 60%,#cde6dc 80%,#8fc8b4 100%)}
.photo.room{background:radial-gradient(ellipse 36% 50% at 50% 38%,#eadbc8 0%,rgba(234,219,200,0) 100%),linear-gradient(180deg,#dfe4ea 0%,#e9ecef 55%,#b9cbe8 80%,#7f9fd8 100%)}
.card .info{height:68px;text-align:center;padding-top:14px}
.card .name{font-size:13.5px;color:var(--text)}
.card .role{font-size:10px;text-transform:uppercase;color:var(--muted);margin-top:2px;letter-spacing:.2px}
.card.active{box-shadow:0 3px 9px rgba(0,0,0,.25)}
.card.active .info{background:var(--teal-soft)}
.card.active .name,.card.active .role{color:var(--white)}
/* footer */
.footer{left:0;top:1518px;width:960px;height:307px;background:var(--foot)}
.footer h4{font-family:'Mulish',sans-serif;font-weight:600;font-size:12.5px;color:var(--text);position:absolute}
.footer ul{list-style:none;position:absolute;font-size:10.5px;line-height:26px;color:var(--text)}
.footer .brand{position:absolute;left:64px;top:66px;font-size:19px}
.footer .addr{position:absolute;left:306px;top:82px;font-size:10.5px;line-height:18px;display:flex;gap:7px}
.footer .contact-line{font-size:10.5px}
.footer .divider{position:absolute;left:64px;top:254px;width:832px;height:1px;background:#bfbfbf}
.footer .legal{position:absolute;left:0;top:275px;width:960px;text-align:center;font-size:8.5px;color:var(--text)}
.legal a{color:var(--teal-bright)}
</style>
</head>
<body>
<div class="page">
  <header class="topbar abs">
    <div class="brand"><span class="dot"></span>Greyfield Ridge Medical</div>
    <div class="contact-line mail">
      <svg width="16" height="12" viewBox="0 0 16 12"><rect x="1" y="1" width="14" height="10" fill="none" stroke="#33b8a4" stroke-width="1.2"/><path d="M1 1l7 6 7-6" fill="none" stroke="#33b8a4" stroke-width="1.2"/></svg>
      hello@greyfieldridge.care
    </div>
    <div class="contact-line phone">
      <svg width="14" height="14" viewBox="0 0 14 14"><path d="M3 1l2 3-1.3 1.3a8 8 0 0 0 5 5L10 9l3 2-1 2c-6 0-11-5-11-11z" fill="none" stroke="#33b8a4" stroke-width="1.1"/></svg>
      (800) 555-0142
    </div>
  </header>

  <nav class="nav abs">
    <a class="current" href="#">HOME</a><a href="#">ABOUT US</a><a href="#">OUR SERVICES</a><a href="#">PATIENTS &amp; VISITORS</a><a href="#">APPOINTMENTS</a><a href="#">NEWS &amp; INFORMATION</a><a href="#">CONTACT US</a>
  </nav>

  <section class="hero abs" role="img" aria-label="Photo of medical staff with stethoscopes in a bright clinic corridor">
    <h1>About <span>Our Practice</span></h1>
  </section>

  <h2 class="section-title abs" style="top:416px">Greyfield Ridge Medical</h2>
  <div class="rule abs" style="left:316px;top:462px"></div>
  <p class="lede abs" style="left:317px;top:476px">But I must explain to you how all this mistaken idea of.</p>
  <p class="body-copy abs" style="left:64px;top:513px;width:405px">Lorem ipsum dolor sit amet, consetetur sadipscing elitr, sed diam nonumy eirmod tempor invidunt ut labore et dolore magna aliquyam erat, sed diam voluptua. At vero eos et accusam et justo duo dolores et ea rebum. Stet clita kasd gubergren, no sea takimata sanctus est Lorem ipsum dolor sit amet. Lorem ipsum dolor sit amet, consetetur sadipscing.</p>
  <p class="body-copy abs" style="left:491px;top:513px;width:405px">Lorem ipsum dolor sit amet, consetetur sadipscing elitr, sed diam nonumy eirmod tempor invidunt ut labore et dolore magna aliquyam erat, sed diam voluptua. At vero eos et accusam et justo duo dolores et ea rebum. Stet clita kasd gubergren, no sea takimata sanctus est Lorem ipsum dolor sit amet. Lorem ipsum dolor sit amet, consetetur sadipscing.</p>

  <section class="team-band abs"></section>
  <h2 class="section-title abs" style="top:704px;left:-13px">Meet The Team</h2>
  <div class="rule abs" style="left:358px;top:747px"></div>
  <p class="lede abs" style="left:262px;top:768px">Lorem ipsum dolor sit amet, consetetur sadipscing elitr, sed diam</p>
  <p class="body-copy abs" style="left:262px;top:792px;width:405px">&nbsp;nonumy eirmod tempor invidunt ut labore et dolore magna aliquyam erat, sed diam voluptua. At vero eos et accusam et justo duo dolores et ea rebum. Stet clita kasd gubergren, no sea takimata sanctus est Lorem ipsum dolor sit amet. Lorem ipsum dolor sit amet, consetetur sadipscing.</p>

  <article class="card active abs" style="left:64px;top:907px"><div class="photo coat" role="img" aria-label="Portrait photo of the family medicine doctor in a white coat"></div><div class="info"><div class="name">Helena Marsh, M.D.</div><div class="role">Family Medicine</div></div></article>
  <article class="card abs" style="left:277px;top:907px"><div class="photo coat-blue" role="img" aria-label="Portrait photo of the internal medicine doctor in a white coat"></div><div class="info"><div class="name">Victor Hale, M.D.</div><div class="role">Internal Medicine</div></div></article>
  <article class="card abs" style="left:491px;top:907px"><div class="photo coat-blue" role="img" aria-label="Portrait photo of the obstetrics doctor in a white coat"></div><div class="info"><div class="name">Victor Hale, M.D.</div><div class="role">Obstetrics &amp; Gynecology</div></div></article>
  <article class="card abs" style="left:705px;top:907px"><div class="photo scrubs-soft" role="img" aria-label="Portrait photo of the nurse practitioner in green scrubs"></div><div class="info"><div class="name">Nora Bellamy, N.P.</div><div class="role">Nurse Practitioner</div></div></article>

  <article class="card abs" style="left:64px;top:1187px"><div class="photo scrubs" role="img" aria-label="Portrait photo of a nurse in teal scrubs"></div><div class="info"><div class="name">Maria Quinn, R.N.</div><div class="role">Nurse</div></div></article>
  <article class="card abs" style="left:277px;top:1189px"><div class="photo scrubs" role="img" aria-label="Portrait photo of a nurse in teal scrubs"></div><div class="info"><div class="name">Lina Ferraro, R.N.</div><div class="role">Nurse</div></div></article>
  <article class="card abs" style="left:491px;top:1189px"><div class="photo scrubs" role="img" aria-label="Portrait photo of a nurse in teal scrubs"></div><div class="info"><div class="name">Carla Wren, R.N.</div><div class="role">Nurse</div></div></article>
  <article class="card abs" style="left:705px;top:1187px"><div class="photo room" role="img" aria-label="Portrait photo of the front desk coordinator in an office"></div><div class="info"><div class="name">Sonia Ashford</div><div class="role">Front Desk</div></div></article>

  <footer class="footer abs">
    <div class="brand"><span class="dot"></span>Greyfield Ridge Medical</div>
    <h4 style="left:326px;top:45px">CONTACT</h4>
    <div class="addr">
      <svg width="12" height="16" viewBox="0 0 12 16"><path d="M6 15s5-5.5 5-9A5 5 0 0 0 1 6c0 3.5 5 9 5 9z" fill="none" stroke="#33b8a4" stroke-width="1.1"/><circle cx="6" cy="6" r="1.8" fill="none" stroke="#33b8a4"/></svg>
      <span>48 Alder Lane<br>Millbrook, AZ 85099</span>
    </div>
    <div class="contact-line abs" style="left:306px;top:137px">
      <svg width="16" height="12" viewBox="0 0 16 12"><rect x="1" y="1" width="14" height="10" fill="none" stroke="#33b8a4" stroke-width="1.2"/><path d="M1 1l7 6 7-6" fill="none" stroke="#33b8a4" stroke-width="1.2"/></svg>
      care@greyfieldridge.care
    </div>
    <div class="contact-line abs" style="left:306px;top:172px">
      <svg width="14" height="14" viewBox="0 0 14 14"><path d="M3 1l2 3-1.3 1.3a8 8 0 0 0 5 5L10 9l3 2-1 2c-6 0-11-5-11-11z" fill="none" stroke="#33b8a4" stroke-width="1.1"/></svg>
      (345) 555-0187
    </div>
    <h4 style="left:597px;top:45px">MENU</h4>
    <ul style="left:599px;top:77px"><li>About Us</li><li>Our Services</li><li>Patients &amp; Visitors</li><li>Appointments</li><li>News &amp; Information</li><li>Contact Us</li></ul>
    <h4 style="left:824px;top:46px">FOLLOW US</h4>
    <ul style="left:824px;top:76px"><li>Friendbook</li><li>Chirper</li><li>Snapgram</li><li>Circles+</li><li>Viewtube</li></ul>
    <div class="divider"></div>
    <p class="legal">©2020 Greyfield Ridge Medical. All Rights Reserved. &nbsp;&nbsp;&nbsp; <a href="#">Disclaimer</a> | <a href="#">Privacy Policy</a></p>
  </footer>
</div>
</body>
</html>
```